Tovex - Business Card Design

Design a modern masculine business card for our business

Target Market(s)

Private Market

Industry/Entity Type

Construction

Contact Information for Business Card

Company Name - Name of Person - Address - email address - contact number

Font styles to use
Serif
Sans Serif

Colors
0094D4
00A9DD
6FCCEA
C7EBF8
E9F6FB
00AB8E
00BBA5
67D7C9
C6EFE9
E9F9F6
F0912C
F2A743
F7CA91
FBE8D2
FDF5EE

Requirements
Must have
• Use company logo provided
Nice to have
• Company Logo

```html
<!DOCTYPE html>
<html lang="en">
<head>
<meta charset="utf-8">
<title>Tovex Construction – Business Card</title>
<link href="https://fonts.googleapis.com/css2?family=Montserrat:wght@700;800&family=Roboto:wght@400&display=swap" rel="stylesheet">
<style>
  :root {
    --backdrop: #232325;
    --card-white: #ffffff;
    --card-black: #060708;
    --ink: #0b0b0c;
    --accent: #f07128;
    --muted: #6d6e70;
    --divider: #8a8a8a;
  }
  * { box-sizing: border-box; margin: 0; padding: 0; }
  html, body {
    width: 1200px; height: 800px; overflow: hidden;
    background: var(--backdrop);
  }
  .sheet {
    position: relative; width: 1200px; height: 800px;
    display: flex; align-items: center; justify-content: center; gap: 40px;
  }
  .card {
    position: relative; width: 540px; height: 310px;
    box-shadow: 0 10px 30px rgba(0,0,0,.45);
  }
  .card--front { background: var(--card-white); }
  .card--back { background: var(--card-black); display: flex; align-items: center; justify-content: center; }

  .wordmark {
    display: flex; align-items: center; gap: 12px;
    font-family: "Montserrat", sans-serif; font-weight: 800;
    letter-spacing: 2px; line-height: 1;
  }
  .wordmark__square { width: 22px; height: 22px; background: var(--accent); }
  .wordmark__name { font-size: 30px; }
  .card--front .wordmark { position: absolute; top: 52px; left: 0; right: 0; justify-content: center; color: var(--ink); }
  .card--back .wordmark { color: var(--card-white); }

  .identity {
    position: absolute; top: 150px; left: 40px; width: 200px; text-align: right;
  }
  .identity__name {
    font-family: "Montserrat", sans-serif; font-weight: 700;
    font-size: 17px; color: var(--ink); letter-spacing: .5px;
  }
  .identity__role {
    font-family: "Roboto", sans-serif; font-size: 16px; color: var(--accent); margin-top: 4px;
  }
  .divider {
    position: absolute; top: 145px; left: 262px; width: 1px; height: 82px; background: var(--divider);
  }
  .contact-list {
    position: absolute; top: 150px; left: 282px; list-style: none;
    font-family: "Roboto", sans-serif; font-size: 15px; color: var(--muted);
  }
  .contact-list li { display: flex; align-items: center; gap: 9px; height: 24px; }
  .contact-list svg, .address svg { width: 14px; height: 14px; flex: none; }
  .address {
    position: absolute; bottom: 42px; left: 100px;
    display: flex; align-items: center; gap: 9px;
    font-family: "Roboto", sans-serif; font-size: 15px; color: var(--muted);
  }
</style>
</head>
<body>
<main class="sheet">
  <section class="card card--front" aria-label="Business card front">
    <div class="wordmark">
      <span class="wordmark__square"></span>
      <span class="wordmark__name">TOVEX CONSTRUCTION, INC</span>
    </div>

    <div class="identity">
      <p class="identity__name">MARCUS T. VELDEN</p>
      <p class="identity__role">Founder &amp; CEO</p>
    </div>
    <div class="divider"></div>

    <ul class="contact-list">
      <li>
        <svg viewBox="0 0 24 24" aria-hidden="true"><path fill="#f07128" d="M6.6 10.8a15 15 0 0 0 6.6 6.6l2.2-2.2c.3-.3.7-.4 1-.2 1.1.4 2.3.6 3.6.6.6 0 1 .4 1 1V20c0 .6-.4 1-1 1A17 17 0 0 1 3 4c0-.6.4-1 1-1h3.5c.6 0 1 .4 1 1 0 1.3.2 2.5.6 3.6.1.3 0 .7-.2 1z"/></svg>
        <span>(555)014-0237</span>
      </li>
      <li>
        <svg viewBox="0 0 24 24" aria-hidden="true"><rect x="2" y="5" width="20" height="14" fill="none" stroke="#f07128" stroke-width="2"/><path d="M2 5l10 8 10-8" fill="none" stroke="#f07128" stroke-width="2"/></svg>
        <span>info@tovexmail.com</span>
      </li>
      <li>
        <svg viewBox="0 0 24 24" aria-hidden="true"><g fill="none" stroke="#f07128" stroke-width="1.6"><circle cx="12" cy="12" r="10"/><ellipse cx="12" cy="12" rx="4.5" ry="10"/><path d="M2 12h20M4 7h16M4 17h16"/></g></svg>
        <span>www.tovexwebsite.com</span>
      </li>
    </ul>

    <p class="address">
      <svg viewBox="0 0 24 24" aria-hidden="true"><path fill="#f07128" d="M12 2a7 7 0 0 0-7 7c0 5 7 13 7 13s7-8 7-13a7 7 0 0 0-7-7zm0 9.5a2.5 2.5 0 1 1 0-5 2.5 2.5 0 0 1 0 5z"/></svg>
      <span>4820 Harbor Ridge Drive, Alden, CA 92700</span>
    </p>
  </section>

  <section class="card card--back" aria-label="Business card back">
    <div class="wordmark">
      <span class="wordmark__square"></span>
      <span class="wordmark__name">TOVEX CONSTRUCTION, INC</span>
    </div>
  </section>
</main>
</body>
</html>
```